8x8 Social Media Ad - Summit Harbor Expo

Attention Real Estate Agents
Please join us for our
Quarterly Real Estate Training Expo
The 2nd Saturday of February, May, August and November
Our Next Training Expo is _________________________________
From 9 am to 1 pm
at
Marlowe Suites Fernfield Oak Ridge
4187 Copper Meadow Lane, Fernfield, MD 20994
Scheduled Speakers
9:00 am - Malcolm Prewitt - Orientation
9:30 am - Darnell Ockley - Multiple Income Streams / Pivot Program
10:00 am - Keira Lindqvist - Marketing though Social Media
10:45 am - Owen Trask - Generating Business through Lumo-Net
11:30 am - Ada Nwachime - Real Estate Investing
12:15 pm - Gregory Tamsin - (Main Speaker) Training Topic TBA
For more information call Malcolm Prewitt at (240) 555-0182 or email mprewitt@summitharborhomes.example

```html
<!DOCTYPE html>
<html lang="en">
<head>
<meta charset="utf-8">
<title>Summit Harbor Expo – Quarterly Real Estate Training Expo</title>
<link rel="stylesheet" href="https://fonts.googleapis.com/css2?family=Anton&family=Poppins:wght@400;500;600;700&display=swap">
<style>
  :root {
    --teal: #17919c;
    --teal-deep: #126f78;
    --ink: #1e1e1e;
    --paper: #ffffff;
    --photo-a: #8a9aa0;
    --photo-b: #3d4a50;
  }
  html, body { margin: 0; padding: 0; overflow: hidden; background: var(--paper); }
  .flyer { display: block; width: 1200px; height: 1200px; }
  .sans { font-family: "Poppins", sans-serif; }
  .display { font-family: "Anton", sans-serif; }
  .invite { fill: var(--paper); font-size: 34px; font-weight: 400; }
  .brand-name { fill: var(--teal); font-weight: 700; }
  .headline { fill: var(--ink); font-size: 212px; }
  .subhead { fill: var(--ink); font-size: 56px; font-weight: 600; }
  .when-title { fill: var(--paper); font-size: 37px; font-weight: 500; }
  .when-small { fill: var(--paper); font-size: 17px; font-weight: 500; }
  .when-months { fill: var(--teal); font-size: 28px; font-weight: 600; }
  .where-title { fill: var(--paper); font-size: 37px; font-weight: 500; }
  .where-line { fill: var(--paper); font-size: 17px; font-weight: 500; }
  .next-expo { fill: var(--ink); font-size: 19px; font-weight: 500; }
  .section-title { fill: var(--paper); font-size: 26px; font-weight: 700; text-anchor: middle; }
  .speaker-name { fill: var(--paper); font-size: 16.5px; font-weight: 500; text-anchor: middle; }
  .speaker-topic { fill: var(--paper); font-size: 13px; font-weight: 400; text-anchor: middle; }
  .speaker-time { fill: var(--paper); font-size: 26px; text-anchor: middle; }
  .divider { stroke: rgba(255,255,255,0.55); stroke-width: 1.5; }
  .info-label { fill: var(--ink); font-size: 16px; font-weight: 600; text-anchor: middle; }
  .contact { fill: var(--paper); font-size: 21px; font-weight: 500; }
</style>
</head>
<body>
<svg class="flyer" viewBox="0 0 1200 1200" xmlns="http://www.w3.org/2000/svg">
  <defs>
    <linearGradient id="skyline-tone" x1="0" y1="0" x2="0" y2="1">
      <stop offset="0" stop-color="var(--teal)" stop-opacity="0.85"/>
      <stop offset="0.6" stop-color="var(--teal-deep)"/>
      <stop offset="1" stop-color="#111111"/>
    </linearGradient>
    <radialGradient id="portrait-tone" cx="0.5" cy="0.4" r="0.6">
      <stop offset="0" stop-color="var(--photo-a)"/>
      <stop offset="1" stop-color="var(--photo-b)"/>
    </radialGradient>
  </defs>

  <rect class="background" width="1200" height="1200" fill="var(--paper)"/>

  <!-- header band -->
  <polygon class="header-band" points="413,0 1198,0 1014,306 208,306" fill="var(--ink)"/>
  <text class="sans invite" x="630" y="58">PLEASE JOIN US FOR OUR</text>

  <!-- brand -->
  <g class="brand sans">
    <text class="brand-name" x="28" y="110" font-size="42">SUMMIT</text>
    <text class="brand-name" x="28" y="150" font-size="30">HARBOR</text>
    <text class="brand-name" x="28" y="182" font-size="19">REALTY GROUP</text>
  </g>

  <!-- city skyline area -->
  <rect class="skyline" x="250" y="96" width="764" height="236" fill="url(#skyline-tone)"
        role="img" aria-label="Teal and black city skyline silhouette with towers and a Ferris wheel"/>

  <!-- headline -->
  <text class="display headline" x="208" y="490" textLength="810" lengthAdjust="spacingAndGlyphs">QUARTERLY</text>
  <text class="sans subhead" x="208" y="568" textLength="800" lengthAdjust="spacingAndGlyphs">REAL ESTATE TRAINING EXPO</text>

  <!-- schedule box -->
  <rect class="when-box" x="205" y="592" width="391" height="133" fill="var(--ink)"/>
  <text class="sans when-title" x="222" y="638">THE 2ND SATURDAY</text>
  <text class="sans when-small" x="224" y="665">of February, May,</text>
  <text class="sans when-months" x="224" y="703">AUGUST &amp; NOVEMBER</text>

  <!-- venue box -->
  <rect class="where-box" x="596" y="592" width="396" height="133" fill="var(--teal)"/>
  <text class="sans where-title" x="622" y="634">FROM 9 AM TO 1 PM</text>
  <text class="sans where-line" x="623" y="658">at Marlowe Suites Fernfield</text>
  <text class="sans where-line" x="623" y="684">Oak Ridge, 4187 Copper Meadow</text>
  <text class="sans where-line" x="623" y="709">Lane, Fernfield, MD 20994</text>

  <text class="sans next-expo" x="206" y="782">Our Next Training Expo is ___________________________________</text>

  <!-- speakers band -->
  <rect class="speakers-band" x="0" y="803" width="1200" height="341" fill="var(--teal)"/>
  <text class="sans section-title" x="605" y="843">SCHEDULED SPEAKERS</text>

  <g class="dividers">
    <line class="divider" x1="208" y1="884" x2="208" y2="1070"/>
    <line class="divider" x1="403" y1="884" x2="403" y2="1070"/>
    <line class="divider" x1="599" y1="884" x2="599" y2="1070"/>
    <line class="divider" x1="796" y1="884" x2="796" y2="1070"/>
    <line class="divider" x1="991" y1="884" x2="991" y2="1070"/>
  </g>

  <g class="speaker sans">
    <circle cx="115" cy="922" r="38" fill="url(#portrait-tone)" stroke="#fff" stroke-width="2" role="img" aria-label="Portrait of Malcolm Prewitt"/>
    <text class="speaker-name" x="115" y="988">MALCOLM PREWITT</text>
    <text class="speaker-topic" x="115" y="1007">Orientation</text>
    <text class="display speaker-time" x="115" y="1056">9:00 AM</text>
  </g>
  <g class="speaker sans">
    <circle cx="303" cy="922" r="38" fill="url(#portrait-tone)" stroke="#fff" stroke-width="2" role="img" aria-label="Portrait of Darnell Ockley"/>
    <text class="speaker-name" x="303" y="988">DARNELL OCKLEY</text>
    <text class="speaker-topic" x="303" y="1007">Multiple Income</text>
    <text class="speaker-topic" x="303" y="1025">Streams / Pivot Program</text>
    <text class="display speaker-time" x="303" y="1058">9:30 AM</text>
  </g>
  <g class="speaker sans">
    <circle cx="505" cy="922" r="38" fill="url(#portrait-tone)" stroke="#fff" stroke-width="2" role="img" aria-label="Portrait of Keira Lindqvist"/>
    <text class="speaker-name" x="505" y="988">KEIRA LINDQVIST</text>
    <text class="speaker-topic" x="505" y="1007">Marketing though</text>
    <text class="speaker-topic" x="505" y="1025">Social Media</text>
    <text class="display speaker-time" x="505" y="1058">10:00 AM</text>
  </g>
  <g class="speaker sans">
    <circle cx="700" cy="922" r="38" fill="url(#portrait-tone)" stroke="#fff" stroke-width="2" role="img" aria-label="Portrait of Owen Trask"/>
    <text class="speaker-name" x="700" y="988">OWEN TRASK</text>
    <text class="speaker-topic" x="700" y="1007">Generating Business</text>
    <text class="speaker-topic" x="700" y="1025">through Lumo-Net</text>
    <text class="display speaker-time" x="700" y="1058">10:45 AM</text>
  </g>
  <g class="speaker sans">
    <circle cx="898" cy="922" r="38" fill="url(#portrait-tone)" stroke="#fff" stroke-width="2" role="img" aria-label="Portrait of Ada Nwachime"/>
    <text class="speaker-name" x="898" y="988">ADA NWACHIME</text>
    <text class="speaker-topic" x="898" y="1007">Real Estate</text>
    <text class="speaker-topic" x="898" y="1025">Investing</text>
    <text class="display speaker-time" x="898" y="1058">11:30AM</text>
  </g>
  <g class="speaker sans">
    <circle cx="1090" cy="922" r="38" fill="url(#portrait-tone)" stroke="#fff" stroke-width="2" role="img" aria-label="Portrait of Gregory Tamsin"/>
    <text class="speaker-name" x="1090" y="988">GREGORY TAMSIN</text>
    <text class="speaker-topic" x="1090" y="1007">(Main Speaker)</text>
    <text class="speaker-topic" x="1090" y="1025">Training Topic TBA</text>
    <text class="display speaker-time" x="1090" y="1058">12:15 PM</text>
  </g>

  <!-- contact -->
  <text class="sans info-label" x="605" y="1107">FOR MORE INFORMATION</text>
  <rect class="contact-bar" x="101" y="1123" width="1016" height="40" fill="var(--ink)"/>
  <text class="sans contact" x="116" y="1151" textLength="986" lengthAdjust="spacingAndGlyphs">CALL MALCOLM PREWITT AT (240) 555-0182 OR EMAIL MPREWITT@SUMMITHARBORHOMES.EXAMPLE</text>
</svg>
</body>
</html>
```